Corvane Project Services - Flyer

Project Breif:
I need a single page A4 Capability Statement, which will be used to market our services to prospective clients, both in print and via email PDF.
It needs to look professional and should incorporate the elements I have uploaded into files, these include:
Capability Statement Text
Corvane Services Company Logo
Additional Logo’s (Tools We Use)
Glimmer Bay Pics can be cut into the page
I have included examples of capability statements as a guide to what i am looking for.
Regards
Derek
Engineering Consulting

```html
<!DOCTYPE html>
<html lang="en">
<head>
<meta charset="utf-8">
<title>Corvane Project Services – Capability Statement</title>
<link href="https://fonts.googleapis.com/css2?family=Montserrat:wght@400;600&family=Arimo:wght@400;700&display=swap" rel="stylesheet">
<style>
:root{
  --backdrop:#e9ecef;
  --paper:#ffffff;
  --sky:#7fc4e6;
  --sky-soft:#bfe2f3;
  --navy:#1c4fa0;
  --ink:#2b2f36;
  --panel:#e6e7e9;
  --charcoal:#3b3d42;
  --muted:#5c6068;
}
*{box-sizing:border-box;margin:0;padding:0}
html,body{width:1200px;height:1200px;overflow:hidden;background:var(--backdrop)}
body{font-family:"Arimo",Arial,sans-serif;color:var(--ink);position:relative}
.flyer{position:absolute;left:204px;top:40px;width:792px;height:1120px;background:var(--paper);overflow:hidden;box-shadow:0 4px 18px rgba(0,0,0,.18)}
.top-strip{position:absolute;left:460px;top:0;width:332px;height:18px;background:var(--sky)}
.hero-photo{position:absolute;left:0;top:0;width:460px;height:232px;background:linear-gradient(135deg,#e8f1f8 0%,#c9dbe9 45%,#9fb9cf 100%)}
.brand{position:absolute;left:470px;top:40px;width:310px;height:140px;display:flex;flex-direction:column;align-items:center;justify-content:center;gap:10px}
.brand-mark{width:52px;height:52px;border-radius:50%;background:var(--navy)}
.brand-name{font-family:"Montserrat",sans-serif;font-weight:600;font-size:19px;letter-spacing:1px;color:var(--ink);text-transform:uppercase;text-align:center;line-height:1.2}
.logo-band{position:absolute;left:460px;top:190px;width:332px;height:42px;background:var(--sky)}
.title-band{position:absolute;left:0;top:232px;width:792px;height:54px;background:var(--sky);display:flex;align-items:center;padding-left:40px}
.title-band h1{font-family:"Montserrat",sans-serif;font-weight:400;font-size:30px;letter-spacing:3px;color:#fff;text-transform:uppercase}
.info-panel{position:absolute;left:0;top:286px;width:792px;height:420px;background:var(--panel)}
.info-frame{position:absolute;left:26px;top:14px;width:740px;height:392px;border:2px solid var(--sky-soft)}
.info-block{position:absolute;left:40px;display:flex;gap:16px;width:700px}
.info-icon{flex:0 0 44px;height:44px;margin-top:22px}
.info-block h2{font-family:"Montserrat",sans-serif;font-weight:600;font-size:19px;letter-spacing:1px;color:var(--navy);text-transform:uppercase;border-bottom:1px dashed var(--sky);padding-bottom:4px;margin-bottom:6px}
.info-block p{font-size:13.5px;line-height:1.45;color:var(--ink)}
.about{top:30px}
.team{top:148px}
.expertise{top:238px}
.services-band{position:absolute;left:0;top:706px;width:792px;height:34px;background:var(--sky)}
.services-title{position:absolute;left:40px;top:690px;font-family:"Montserrat",sans-serif;font-weight:600;font-size:21px;letter-spacing:1px;color:var(--navy);background:var(--panel);padding:0 10px}
.service-col{position:absolute;top:716px}
.service-col h3{font-size:13px;font-weight:700;color:var(--ink);margin-bottom:14px}
.service-col ul{list-style:none}
.service-col li{font-size:11.5px;line-height:1.6;padding-left:14px;position:relative;white-space:nowrap}
.service-col li::before{content:"";position:absolute;left:0;top:5px;border-left:6px solid var(--navy);border-top:4px solid transparent;border-bottom:4px solid transparent}
.col-plan{left:50px}
.col-risk{left:305px}
.col-cost{left:575px}
.divider{position:absolute;left:40px;top:890px;width:712px;border-top:1px dashed var(--sky)}
.tools{position:absolute;left:330px;top:908px;width:440px;display:grid;grid-template-columns:repeat(3,1fr);gap:16px 14px;align-items:center}
.tool{font-family:"Arimo",sans-serif;font-weight:700;font-size:15px;color:var(--muted);display:flex;align-items:center;gap:6px;white-space:nowrap}
.tool i{width:10px;height:10px;background:var(--muted);display:inline-block}
.placeholder-logo{position:absolute;left:50px;top:930px;font-family:"Montserrat",sans-serif;font-size:22px;letter-spacing:2px;color:var(--sky);line-height:1.2;text-transform:uppercase}
.web-bar{position:absolute;left:250px;top:1010px;width:542px;height:46px;background:var(--sky);display:flex;align-items:center;justify-content:space-around;color:#fff;font-size:14px}
.contact-bar{position:absolute;left:0;top:1066px;width:792px;height:54px;background:var(--sky);display:flex;align-items:center}
.contact-label{height:54px;width:200px;background:var(--charcoal);color:var(--sky);font-family:"Montserrat",sans-serif;font-size:22px;letter-spacing:2px;display:flex;align-items:center;justify-content:center}
.contact-item{display:flex;align-items:center;gap:8px;color:#fff;font-size:14px;padding-left:24px}
.contact-item svg,.web-bar svg{width:16px;height:16px}
</style>
</head>
<body>
<main class="flyer">
  <div class="hero-photo" role="img" aria-label="Photo of a team reviewing printed project charts and documents at a desk"></div>
  <div class="top-strip"></div>
  <div class="brand">
    <div class="brand-mark"></div>
    <div class="brand-name">Corvane Project<br>Services</div>
  </div>
  <div class="logo-band"></div>
  <div class="title-band"><h1>Capability Statement</h1></div>

  <section class="info-panel">
    <div class="info-frame"></div>
    <article class="info-block about">
      <svg class="info-icon" viewBox="0 0 44 44"><circle cx="22" cy="22" r="22" fill="#3b3d42"/><circle cx="16" cy="17" r="5" fill="#fff"/><circle cx="28" cy="17" r="5" fill="#fff"/><path d="M8 32c0-6 4-9 8-9s8 3 8 9zM20 32c0-6 4-9 8-9s8 3 8 9z" fill="#fff"/></svg>
      <div><h2>About Us:</h2>
      <p>Our goal is to make successful project delivery more achievable and repeatable. We are continually innovating, evolving and learning, utilizing the latest industry tools and techniques to deliver real value to our clients. We are passionate about empowering organisations to achieve their objectives, on time and on budget.</p></div>
    </article>
    <article class="info-block team">
      <svg class="info-icon" viewBox="0 0 44 44"><circle cx="22" cy="22" r="22" fill="#3b3d42"/><circle cx="22" cy="12" r="4" fill="#fff"/><circle cx="12" cy="26" r="4" fill="#fff"/><circle cx="32" cy="26" r="4" fill="#fff"/><circle cx="22" cy="34" r="3" fill="#fff"/></svg>
      <div><h2>Our Team</h2>
      <p>We use highly experienced industry professionals who engage with our clients to deliver practical and innovative project control solutions.</p></div>
    </article>
    <article class="info-block expertise">
      <svg class="info-icon" viewBox="0 0 44 44"><circle cx="22" cy="22" r="22" fill="#3b3d42"/><circle cx="22" cy="21" r="10" fill="none" stroke="#fff" stroke-width="3"/><circle cx="22" cy="21" r="3" fill="#fff"/></svg>
      <div><h2>Our Expertise</h2>
      <p>For over 20 years we have been helping our clients to successfully deliver capital projects within the pharmaceutical and biotechnology sectors. During this time, we have worked closely with multinational healthcare companies and leading A&amp;E firms, on a variety of business-critical projects. Our experience and knowledge of project control gives our client's unparalleled visibility of Cost, Schedule and Risk through the lifecycle of their projects. This visibility allows our clients to make timely informed decisions which increase efficiency and project performance.</p></div>
    </article>
  </section>

  <div class="services-band"></div>
  <h2 class="services-title">CORE SERVICES:</h2>
  <section class="service-col col-plan">
    <h3>Planning and Scheduling</h3>
    <ul><li>Tender Planning</li><li>Interactive Planning / Pull Planning</li><li>CPM Planning &amp; Scheduling</li><li>Agile / Lean Planning Methodology</li><li>Independent Schedule Quality Assessment</li><li>Schedule Risk Analysis (Monte Carlo)</li><li>Training</li></ul>
  </section>
  <section class="service-col col-risk">
    <h3>Management of Risk</h3>
    <ul><li>Risk Management Policies &amp; Procedures</li><li>Risk Management Strategy</li><li>Risk Registers</li><li>Risk Response and Communication</li><li>Cost &amp; Schedule Risk Analysis (Monte Carlo)</li><li>Risk Management Training</li></ul>
  </section>
  <section class="service-col col-cost">
    <h3>Cost Control:</h3>
    <ul><li>Estimating &amp; Forecasting</li><li>Earned Value Management</li><li>Progress Reporting</li><li>Cost Risk Analysis (Monte Carlo)</li></ul>
  </section>

  <div class="divider"></div>
  <div class="placeholder-logo">Services<br>Company Logo</div>
  <section class="tools" aria-label="Tools we use">
    <span class="tool"><i></i>Orrel Plan Suite</span>
    <span class="tool"><i></i>Taskplan</span>
    <span class="tool"><i></i>Astrel Scheduler</span>
    <span class="tool"><i></i>Waymark Pro</span>
    <span class="tool"><i></i>Dalvern Metric</span>
    <span class="tool"><i></i>RiskFrame</span>
  </section>

  <div class="web-bar">
    <span class="contact-item"><svg viewBox="0 0 16 16"><circle cx="8" cy="8" r="6.5" fill="none" stroke="#fff" stroke-width="1.5"/><path d="M1.5 8h13M8 1.5c-3 3.5-3 9.5 0 13M8 1.5c3 3.5 3 9.5 0 13" fill="none" stroke="#fff" stroke-width="1.2"/></svg>www.corvaneservices.ie</span>
    <span class="contact-item"><svg viewBox="0 0 16 16"><path d="M4 1.5l2.5 3-1.5 1.5c.8 2 2.5 3.7 4.5 4.5L11 9l3 2.5-1.5 2.5C7 14 2 9 1.5 3.5z" fill="#fff"/></svg>+353 (0)87 555 0142</span>
  </div>
  <footer class="contact-bar">
    <div class="contact-label">CONTACT:</div>
    <span class="contact-item"><svg viewBox="0 0 16 16"><rect x="1" y="3" width="14" height="10" fill="none" stroke="#fff" stroke-width="1.5"/><path d="M1 3l7 6 7-6" fill="none" stroke="#fff" stroke-width="1.5"/></svg>info@corvaneservices.ie</span>
  </footer>
</main>
</body>
</html>
```